Logo is done, need templates now

I want to be able to have an email template, same for word documents, powerpoint etc. I have the logo, now I need all the pieces for appearance in correspondence and marketing

Target Market(s)

Professional Advisors and Wealthy Clients

Font styles to use
Serif

Requirements
Must have
• I want to be able to do word documents and email them with letterhead. I need great email signatures. I need similar formatting for the word documents to be flexible to add to powerpoint and other presentations.

```html
<!DOCTYPE html>
<html lang="en">
<head>
<meta charset="utf-8">
<title>Quietvale Capital — Letterhead</title>
<link href="https://fonts.googleapis.com/css2?family=Playfair+Display:wght@400&display=swap" rel="stylesheet">
<style>
  :root {
    --gold-dark: #8a5e31;
    --gold-mid: #c99e65;
    --gold-light: #f4cf98;
    --gold-deep: #a66f32;
    --gold-text: #b58c5a;
    --paper: #ffffff;
    --ink-light: #ffffff;
    --gold-gradient: linear-gradient(90deg, var(--gold-dark) 0%, var(--gold-mid) 30%, var(--gold-light) 48%, var(--gold-mid) 72%, var(--gold-deep) 100%);
  }
  * { margin: 0; padding: 0; box-sizing: border-box; }
  html, body { width: 835px; height: 1200px; overflow: hidden; background: var(--paper); }
  .letterhead {
    position: relative;
    width: 835px;
    height: 1200px;
    background: var(--paper);
    font-family: "Playfair Display", Georgia, serif;
  }
  .masthead {
    position: absolute;
    left: 0; top: 0;
    width: 100%; height: 186px;
    background: var(--gold-gradient);
    text-align: center;
    color: var(--ink-light);
  }
  .brand-name {
    position: absolute;
    left: 0; right: 0; top: 98px;
    font-size: 19px;
    font-weight: 400;
    letter-spacing: 0.32em;
    padding-left: 0.32em;
    text-transform: uppercase;
    line-height: 1;
  }
  .address {
    position: absolute;
    left: 0; right: 0; top: 144px;
    font-size: 16px;
    line-height: 1;
  }
  .rule {
    position: absolute;
    left: 0;
    width: 100%;
    height: 2.5px;
    background: var(--gold-gradient);
  }
  .rule--head { top: 201px; }
  .rule--foot-upper { top: 1078px; }
  .rule--foot-lower { top: 1093px; }
  .body-area {
    position: absolute;
    left: 60px; right: 60px;
    top: 230px; bottom: 140px;
  }
  .contact {
    position: absolute;
    left: 0; right: 0;
    text-align: center;
    font-size: 16px;
    line-height: 1;
    color: var(--gold-text);
  }
  .contact--phone { top: 1115px; }
  .contact--web { top: 1151px; }
</style>
</head>
<body>
  <main class="letterhead">
    <header class="masthead">
      <div class="brand-name">Quietvale Capital</div>
      <div class="address">Adress</div>
    </header>
    <div class="rule rule--head"></div>

    <section class="body-area"></section>

    <div class="rule rule--foot-upper"></div>
    <div class="rule rule--foot-lower"></div>
    <footer>
      <div class="contact contact--phone">Phone</div>
      <div class="contact contact--web">Website</div>
    </footer>
  </main>
</body>
</html>
```